Custom Home Builder Needs a Website

Harbor Pine Builders Ltd. requires a clean professional 5 page website - Home, About Us, Gallery (Interior and Exterior), Our Process and Contact Us(with registration form). We are a home builder who also has homes for sale. Also please have a place for video embedding. Editable fields by user. Using the stationery 'feel' that is attached. Need social media links. If you require any additional files, please request.

Target Market(s)

Families and professionals

Industry/Entity Type

Home Builder

Coding

Coded - Design and coding required

Number of Pages Required

5+ page

Font styles to use
Sans Serif
Other font styles liked:
• Lato

Requirements
Must have
• Editable by user
• Register Button
• Place to put home models for sale - preferably on the first page
• 5 page website -
• -Home
• -About Us
• -Gallery (Interior and Exterior)
• -Our Process
• -Contact Us.
Nice to have
• Themed similar to current stationery
• place for video embedding
• Try some darker backgrounds
• Change pictures to B/W if works for design
Should not have
• cartoonish type of content

```html
<!DOCTYPE html>
<html lang="en">
<head>
<meta charset="utf-8">
<title>Harbor Pine Builders Ltd.</title>
<link href="https://fonts.googleapis.com/css2?family=Lato:wght@300;400;700&display=swap" rel="stylesheet">
<style>
:root{
  --green:#76a23f;
  --green-dark:#5f8a2e;
  --text:#444;
  --muted:#8a8a8a;
  --footer:#3b3b3b;
  --white:#fff;
}
*{margin:0;padding:0;box-sizing:border-box}
html,body{width:728px;height:1200px;overflow:hidden;background:var(--white)}
body{position:relative;font-family:'Lato',sans-serif;color:var(--text)}
.abs{position:absolute}

.contact-left{left:80px;top:20px;font-size:8px;line-height:15px;color:#333}
.contact-left div{display:flex;align-items:center;gap:6px}
.contact-right{right:80px;top:20px;font-size:8px;line-height:15px;text-align:right;color:#333}
.brand{left:0;width:728px;top:22px;text-align:center;font-size:17px;font-weight:700;color:#2e5a2a;letter-spacing:.5px}
.brand-mark{display:inline-block;width:8px;height:8px;background:var(--green);margin-right:7px;vertical-align:2px}

.hero{left:0;top:82px;width:728px;height:290px;background:linear-gradient(180deg,#a8c3de 0%,#b9b3a1 28%,#5a5a5e 55%,#6f6d64 80%,#8c9a6c 100%)}
.hero-arrow{top:217px;width:15px;height:20px;background:rgba(40,40,40,.7)}
.nav{left:80px;top:70px;width:568px;height:24px;background:var(--green);display:flex;justify-content:center;gap:0}
.nav a{color:var(--white);text-decoration:none;font-size:7.5px;line-height:24px;padding:0 17px}
.nav a.active{text-decoration:underline}

.intro{left:80px;width:568px;top:417px;text-align:center;font-size:12.5px;font-weight:300;line-height:16.5px;color:#444}

.service{top:482px;width:260px;text-align:center}
.service h2{font-size:15px;font-weight:400;color:var(--green);margin-top:4px}
.service p{font-size:6.6px;line-height:12px;color:var(--muted);margin-top:3px}
.btn{display:inline-block;margin-top:10px;border:1px solid #ccc;font-size:6px;color:#666;padding:6px 8px;letter-spacing:.2px}

.video{left:80px;top:645px;width:567px;height:218px;background:linear-gradient(100deg,#d9d6cf 0%,#a79d8c 35%,#cfcbc2 60%,#8a8a86 100%)}
.video-title{left:0;width:728px;top:725px;text-align:center;color:var(--white);font-size:13px;font-weight:700;text-shadow:0 1px 3px rgba(0,0,0,.5)}
.play{left:349px;top:749px}

.gallery-title{left:0;width:728px;top:907px;text-align:center;font-size:15px;color:var(--green)}
.thumb{top:940px;width:135px;height:116px}
.dots{left:0;width:728px;top:1073px;display:flex;justify-content:center;gap:9px}
.dots span{width:5px;height:5px;border-radius:50%;background:#ccc}
.dots span.on{background:var(--green)}

.footer{left:0;top:1127px;width:728px;height:73px;background:var(--footer)}
.footer-links{left:80px;top:1150px;font-size:7px;color:var(--white)}
.footer-links span{margin:0 5px;color:#bbb}
.copyright{left:80px;top:1167px;font-size:6.5px;color:#999}
.social{top:1150px;width:24px;height:24px;border:1px solid #999;border-radius:50%}
</style>
</head>
<body>

<div class="abs contact-left">
  <div><svg width="6" height="8" viewBox="0 0 6 8"><rect x=".5" y=".5" width="5" height="7" rx="1" fill="none" stroke="#333"/></svg>306-555-0142</div>
  <div><svg width="6" height="5" viewBox="0 0 6 5"><rect width="6" height="5" fill="#555"/><path d="M0 0l3 2.5L6 0" stroke="#fff" stroke-width=".7" fill="none"/></svg>info@harborpinebuilders.ca</div>
</div>
<div class="abs brand"><span class="brand-mark"></span>Harbor Pine Builders Ltd.</div>
<div class="abs contact-right">PO Box 208<br>Lakeview, Sk, S0K 2B0</div>

<div class="abs hero" role="img" aria-label="Photo of a craftsman-style house with stone trim and double garage"></div>
<div class="abs hero-arrow" style="left:0"><svg width="15" height="20"><path d="M9 5l-4 5 4 5" stroke="#fff" fill="none"/></svg></div>
<div class="abs hero-arrow" style="right:0"><svg width="15" height="20"><path d="M6 5l4 5-4 5" stroke="#fff" fill="none"/></svg></div>

<nav class="abs nav">
  <a class="active" href="#">HOME</a><a href="#">ABOUT US</a><a href="#">GALLERY</a><a href="#">OUR PROCESS</a><a href="#">CONTACT US</a>
</nav>

<p class="abs intro">Proin sit amet nunc eleifend lacus pretium posuere ut at sem. Sed cursus ligula id libero pretium posuere. Sed consequat turpis sem, et hendrerit dolor posuere non.</p>

<section class="abs service" style="left:92px">
  <svg width="30" height="28" viewBox="0 0 30 28"><path d="M15 1L1 14h4v13h7v-8h6v8h7V14h4z" fill="var(--green)"/></svg>
  <h2>Home Builder</h2>
  <p>Nam fringilla vulputate libero ut porttitor. In id vulputate mauris, at convallis magna. Mauris luctus elementum ante, sed congue dolor accumsan commodo. Cras dictum consectetur mauris, eu pellentesque felis maximus</p>
  <span class="btn">READ MORE</span>
</section>
<section class="abs service" style="left:376px">
  <svg width="30" height="28" viewBox="0 0 30 28"><path d="M4 2h10l14 14-10 10L4 12z" fill="var(--green)"/><circle cx="9" cy="7" r="2" fill="#fff"/></svg>
  <h2>Homes for Sale</h2>
  <p>Nam fringilla vulputate libero ut porttitor. In id vulputate mauris, at convallis magna. Mauris luctus elementum ante, sed congue dolor accumsan commodo. Cras dictum consectetur mauris, eu pellentesque felis maximus</p>
  <span class="btn">READ MORE</span>
</section>

<div class="abs video" role="img" aria-label="Video still of a bright kitchen with granite island and steel fridge"></div>
<div class="abs video-title">FEATURED VIDEO</div>
<svg class="abs play" width="30" height="30" viewBox="0 0 30 30"><circle cx="15" cy="15" r="14" fill="#fff"/><path d="M12 9l9 6-9 6z" fill="#333"/></svg>

<h2 class="abs gallery-title">Gallery</h2>
<div class="abs thumb" style="left:80px;background:linear-gradient(180deg,#b7bcc2,#6d6458 60%,#55534e)" role="img" aria-label="Two-storey home with garage"></div>
<div class="abs thumb" style="left:224px;background:linear-gradient(180deg,#c9ccd0,#6a655e 55%,#5d7c3c)" role="img" aria-label="Large home with front lawn"></div>
<div class="abs thumb" style="left:368px;background:linear-gradient(180deg,#8b8075,#a79e92 50%,#4a4a4a)" role="img" aria-label="Kitchen stove with mosaic backsplash"></div>
<div class="abs thumb" style="left:512px;background:linear-gradient(180deg,#8a8d7e,#6f6d6a 50%,#7a4f3f)" role="img" aria-label="Home with balcony and brick base"></div>
<div class="abs dots"><span class="on"></span><span></span><span></span><span></span><span></span></div>

<footer class="abs footer"></footer>
<div class="abs footer-links">HOME<span>|</span>ABOUT US<span>|</span>GALLERY<span>|</span>OUR PROCESS<span>|</span>CONTACT US</div>
<div class="abs copyright">Copyright © 2016 Company name. All rights reserved.</div>
<a class="abs social" style="left:566px" aria-label="Social link 1"></a>
<a class="abs social" style="left:595px" aria-label="Social link 2"></a>
<a class="abs social" style="left:624px" aria-label="Social link 3"></a>

</body>
</html>
```